design 4x6 flyer - SIMPLE EASY QUICK JOB

(((USE ATTACHED FLYER TEMPLATE)))

Create 4x6 flyer from KTLWcard attachment

SAME design

VIEW KTLWflyer attachment for details

```html
<!DOCTYPE html>
<html lang="en">
<head>
<meta charset="utf-8">
<title>Kite Hill Event Rentals – Flyer</title>
<link rel="stylesheet" href="https://fonts.googleapis.com/css2?family=Bubblegum+Sans&family=Comic+Neue:ital,wght@1,700&display=swap">
<style>
  :root {
    --page-bg: #e9e9e7;
    --card-bg: #ffffff;
    --brand-blue: #5b86c4;
    --brand-red: #e0605e;
    --band-green: #a8cf6c;
    --ink-dark: #333333;
    --phone-white: #ffffff;
    --art-red: #ec7a78;
    --art-yellow: #f6c24e;
    --art-green: #9fd06d;
    --art-blue: #6c9fd6;
  }
  * { margin: 0; padding: 0; box-sizing: border-box; }
  html, body {
    width: 800px;
    height: 1200px;
    overflow: hidden;
    background: var(--page-bg);
  }
  .flyer {
    position: absolute;
    left: 20px;
    top: 347px;
    width: 760px;
    height: 507px;
    background: var(--card-bg);
    box-shadow: 0 4px 14px rgba(0,0,0,0.18);
    overflow: hidden;
    font-family: "Bubblegum Sans", cursive;
    font-variant: small-caps;
  }
  .hero-art {
    position: absolute;
    left: 35px;
    top: 62px;
    width: 252px;
    height: 196px;
  }
  .brand-name {
    position: absolute;
    left: 300px;
    top: 74px;
    width: 450px;
    text-align: center;
    color: var(--brand-blue);
    font-size: 54px;
    line-height: 58px;
  }
  .tagline {
    position: absolute;
    left: 300px;
    top: 202px;
    width: 450px;
    text-align: center;
    color: var(--brand-red);
    font-size: 31px;
    line-height: 38px;
  }
  .services {
    position: absolute;
    left: 0;
    top: 312px;
    width: 760px;
    text-align: center;
    font-family: "Comic Neue", cursive;
    font-style: italic;
    font-weight: 700;
    font-variant: normal;
    text-transform: uppercase;
    font-size: 16px;
    color: var(--ink-dark);
    letter-spacing: -0.2px;
  }
  .owners {
    position: absolute;
    left: 0;
    top: 352px;
    width: 760px;
    text-align: center;
    color: var(--brand-blue);
    font-size: 34px;
    line-height: 1;
  }
  .contact-band {
    position: absolute;
    left: 0;
    top: 403px;
    width: 760px;
    height: 104px;
    background: var(--band-green);
  }
  .phone {
    position: absolute;
    top: 18px;
    font-size: 52px;
    line-height: 1;
    font-variant: normal;
    color: var(--phone-white);
    -webkit-text-stroke: 5px var(--ink-dark);
    paint-order: stroke fill;
    letter-spacing: 1px;
  }
  .phone-first { left: 38px; }
  .phone-second { right: 36px; }
</style>
</head>
<body>
  <main class="flyer">
    <svg class="hero-art" role="img" aria-label="Illustration of children jumping in a colourful bounce castle" viewBox="0 0 252 196">
      <defs>
        <linearGradient id="castleTone" x1="0" y1="0" x2="0" y2="1">
          <stop offset="0" stop-color="var(--art-red)"/>
          <stop offset="0.35" stop-color="var(--art-yellow)"/>
          <stop offset="0.65" stop-color="var(--art-green)"/>
          <stop offset="0.85" stop-color="var(--art-blue)"/>
          <stop offset="1" stop-color="var(--art-red)"/>
        </linearGradient>
      </defs>
      <rect x="0" y="0" width="252" height="196" rx="22" fill="url(#castleTone)" opacity="0.85"/>
    </svg>

    <h1 class="brand-name">Kite Hill<br>Event Rentals</h1>

    <p class="tagline">Bright Days and Big Smiles<br>for Every Celebration</p>

    <p class="services">Bounce Houses - Tables - Chairs - Cotton Candy, Pop Corn &amp; Snow Cone Machines</p>

    <p class="owners">Kevin Tolland &amp; Tyler Whitmore</p>

    <div class="contact-band">
      <span class="phone phone-first">555.214.0187</span>
      <span class="phone phone-second">555.362.7740</span>
    </div>
  </main>
</body>
</html>
```